Turm7Zwerge
Zielgruppe
Zielgruppe sind die Eltern, Lehrer, Kindergärtner, aber auch Kinder, die bereits Lesen können.
Aufgabenstellung
Ich brauche einen Flyer und ein Plakat für eine Kinderschachschule für Kinder zwischen 4 und 15 Jahren. Auf dem Flyer, den ich in A6-Format drucken möchte (beidseitig), muss ich die Info über die Kinderschachschule Turm7Zwerge (mehr Infos unter www.turm7zwerge-beispiel.ch), dh., was wir machen, Kontaktdaten, etc schreiben können. Es dient als Werbematerial zum Auslegen
Auf dem Plakat wird mehr oder weniger das Gleiche stehen, es wird jedoch als Din A4 Seite aufgehängt.
Unsere Kontaktinformation ist wie folgt:
Turm7Zwerge: Spielen mit kleinen Strategen
www.turm7zwerge-beispiel.ch

```html
<!DOCTYPE html>
<html lang="de">
<head>
<meta charset="utf-8">
<title>Turm7Zwerge – Flyer</title>
<link href="https://fonts.googleapis.com/css2?family=Open+Sans:ital,wght@0,400;0,600;0,700;1,700;1,800&display=swap" rel="stylesheet">
<style>
  :root {
    --gold: #c98a10;
    --blue: #1e9ad6;
    --magenta: #c4127a;
    --yellow: #d9a21c;
    --ink: #1b1b1b;
    --text: #2e2e2e;
    --white: #ffffff;
    --board-light: #f6f6f6;
    --board-dark: #e6e6e6;
  }
  * { margin: 0; padding: 0; box-sizing: border-box; }
  html, body { width: 1200px; height: 1200px; overflow: hidden; background: var(--white); }
  body { font-family: "Open Sans", Arial, sans-serif; color: var(--text); }

  .flyer { position: relative; width: 1200px; height: 1200px; overflow: hidden; }

  .board-backdrop {
    position: absolute; left: 362px; top: 290px; width: 838px; height: 720px;
    background: linear-gradient(160deg, var(--board-light) 0%, var(--board-dark) 55%, var(--white) 100%);
  }

  .side-band { position: absolute; left: 0; top: 0; width: 362px; height: 1200px; background: var(--gold); }

  .brand-block {
    position: absolute; left: 0; top: 0; width: 362px; height: 234px; background: var(--white);
    display: flex; flex-direction: column; justify-content: center; padding-left: 40px;
  }
  .brand-name { display: flex; align-items: center; gap: 12px; font-weight: 700; font-size: 42px; color: var(--magenta); line-height: 1; }
  .brand-square { flex: none; width: 24px; height: 24px; background: var(--magenta); }
  .brand-tagline { margin-top: 14px; font-weight: 700; font-size: 19px; color: var(--ink); }

  .headline {
    position: absolute; left: 398px; top: 88px; font-style: italic; font-weight: 800;
    font-size: 48px; line-height: 1.18; color: var(--blue);
  }

  .photo {
    position: absolute; border: 5px solid var(--blue); background: var(--white); padding: 8px;
    box-shadow: 0 4px 12px rgba(0,0,0,0.25);
  }
  .photo .fill { width: 100%; height: 100%; background: linear-gradient(135deg, #3a3a3a 0%, #8a7b68 45%, #d8d2c4 70%, #4a4036 100%); }
  .photo--main { left: 124px; top: 330px; width: 400px; height: 305px; transform: rotate(-5deg); }
  .photo--small { left: 840px; top: 718px; width: 330px; height: 222px; transform: rotate(-8deg); }

  .slogans { position: absolute; left: 0; top: 0; width: 1200px; height: 620px; }
  .slogan { position: absolute; font-style: italic; font-weight: 800; font-size: 43px; line-height: 58px; color: var(--ink); white-space: nowrap; }
  .slogan--fun { left: 640px; top: 312px; }
  .slogan--smart { left: 628px; top: 414px; }
  .slogan--strong { left: 648px; top: 516px; }

  .offer-title { position: absolute; left: 390px; top: 668px; font-style: italic; font-weight: 800; font-size: 28px; color: var(--ink); }
  .offer-list { position: absolute; left: 398px; top: 722px; list-style: none; }
  .offer-list li { display: flex; align-items: center; gap: 14px; height: 45px; font-size: 24px; color: var(--text); }
  .offer-list svg { width: 30px; height: 26px; flex: none; }

  .intro {
    position: absolute; left: 397px; top: 1022px; width: 780px; font-size: 21.5px; line-height: 37px; color: var(--text);
  }

  .vertical-url {
    position: absolute; left: 40px; top: 1140px; transform: rotate(-90deg); transform-origin: left top;
    font-size: 25px; line-height: 32px; font-weight: 600; letter-spacing: 3px; color: var(--white); white-space: nowrap;
  }

  .contact { position: absolute; left: 100px; top: 852px; color: var(--white); white-space: nowrap; }
  .contact-label { font-weight: 700; font-size: 16px; }
  .contact-brand { margin-top: 8px; font-weight: 700; font-size: 24px; }
  .contact-address { margin-top: 10px; font-size: 19px; line-height: 31px; }
  .contact-lines { margin-top: 40px; font-size: 17px; line-height: 27px; }
</style>
</head>
<body>
<main class="flyer">
  <div class="board-backdrop" role="img" aria-label="Heller Schachbrett-Hintergrund"></div>

  <aside class="side-band">
    <div class="brand-block">
      <div class="brand-name"><span class="brand-square"></span>Turm7Zwerge</div>
      <div class="brand-tagline">Spielen mit kleinen Strategen</div>
    </div>
    <div class="vertical-url">www.turm7zwerge-beispiel.ch</div>
    <div class="contact">
      <div class="contact-label">Unsere Kontaktdaten:</div>
      <div class="contact-brand">Turm7Zwerge</div>
      <div class="contact-address">Lindenweg 12<br>Postfach 314<br>8799 Musterdorf</div>
      <div class="contact-lines">Tel.: 079 - 000 12 34<br>info@turm7zwerge-beispiel.ch<br>www.turm7zwerge-beispiel.ch</div>
    </div>
  </aside>

  <h1 class="headline">Wir bringen Ihr Kind<br>Zug um Zug zum Erfolg!</h1>

  <div class="photo photo--main"><div class="fill" role="img" aria-label="Foto: zwei Kinder spielen Schach an einem Tisch"></div></div>

  <svg class="slogans" viewBox="0 0 1200 620" aria-hidden="true">
    <path d="M540 404 C 620 372, 820 364, 1100 368 C 830 374, 660 382, 540 404 Z" fill="var(--magenta)"/>
    <path d="M576 506 C 656 474, 856 466, 1100 470 C 866 476, 696 484, 576 506 Z" fill="var(--yellow)"/>
    <path d="M584 608 C 664 576, 864 568, 1104 572 C 874 578, 704 586, 584 608 Z" fill="var(--blue)"/>
  </svg>
  <div class="slogan slogan--fun">Schach macht Spass!</div>
  <div class="slogan slogan--smart">Schach macht schlau!</div>
  <div class="slogan slogan--strong">Schach macht stark!</div>

  <h2 class="offer-title">Wir bieten Ihrem Kind:</h2>
  <ul class="offer-list">
    <li><svg viewBox="0 0 30 26"><path d="M2 14 L11 23 L28 3" fill="none" stroke="var(--magenta)" stroke-width="5" stroke-linecap="round" stroke-linejoin="round"/></svg>Konzentrationstraining</li>
    <li><svg viewBox="0 0 30 26"><path d="M2 14 L11 23 L28 3" fill="none" stroke="var(--magenta)" stroke-width="5" stroke-linecap="round" stroke-linejoin="round"/></svg>Intellektuelle Förderung</li>
    <li><svg viewBox="0 0 30 26"><path d="M2 14 L11 23 L28 3" fill="none" stroke="var(--magenta)" stroke-width="5" stroke-linecap="round" stroke-linejoin="round"/></svg>Stärkung des Selbstvertrauens</li>
    <li><svg viewBox="0 0 30 26"><path d="M2 14 L11 23 L28 3" fill="none" stroke="var(--magenta)" stroke-width="5" stroke-linecap="round" stroke-linejoin="round"/></svg>Persönliches Wachstum</li>
    <li><svg viewBox="0 0 30 26"><path d="M2 14 L11 23 L28 3" fill="none" stroke="var(--magenta)" stroke-width="5" stroke-linecap="round" stroke-linejoin="round"/></svg>Spass und Spannung</li>
  </ul>

  <div class="photo photo--small"><div class="fill" role="img" aria-label="Foto: Kinder beim Schachspiel"></div></div>

  <p class="intro">Schach ist eine Lebensschule, die das Leben Ihres Kindes nachhaltig positiv verändert. Die Kinder eignen sich spielerisch wesentliche Fähigkeiten an, die sie sowohl im sozialen als auch im schulischen Umfeld zu Höchstleistungen befähigen.</p>
</main>
</body>
</html>
```